Kestrelwood Pathways Agency business cards

Australian company about to start offering its services. We recruit international students to come to study English, vocational education and postgraduate courses in Australia. We help them find the institution and select the right city they want to come to Australia. We are a young, online oriented and supportive agency. Our clients are between 18 and 35 years old, mainly University students, young professionals or people with work experience. We provide much more information that any other agency offer. We administrate a Facebook group with more than 11.000 members that daily ask questions about general information when coming to Australia, while they are here and even after they leave the country

Target Market(s)

International students from South America, Central America and Europe

Industry/Entity Type

Student

Contact Information for Business Card

Tomas Brevik
Managing Director
tomas@velmorin.com.au
www.velmorin.com.au
+61 491058263
Melbourne, Australia

Font styles to use
Serif
Sans Serif

Colors

Designer to choose colors to be used in the design.

Requirements
Must have
• Horizontal design
• Standard business card size and shape. If font uses green or yellow colours, they will have to match the ones from the logo
Nice to have
• UPDATE: Use the contents of the green image to design one of the card sides. Use our logo in the background of that side as watermark.
• Passport image, or immigration stamps. A picture of the Yarra River (from Melbourne) would be cool as well.
Should not have
• Non-standard business card size and shape
• Not black as the background colour of any sides as we are not a VIP agency or a hight class service. We are orientes to young people and they like colours, pictures, something attractive.
• Vertical design
• NO YELLOW or BLACK AS THE BACKGROUND COLOUR OF ANY SIDE OF THE BIZ CARD

```html
<!DOCTYPE html>
<html lang="en">
<head>
<meta charset="utf-8">
<title>Kestrelwood Pathways Agency — Business Cards</title>
<link href="https://fonts.googleapis.com/css2?family=Roboto:wght@400;500;700&display=swap" rel="stylesheet">
<style>
  :root {
    --brand-green: #0b6544;
    --brand-yellow: #e8b923;
    --card-white: #ffffff;
    --ink: #1c1c1c;
    --stage: #5d6468;
  }
  * { margin: 0; padding: 0; box-sizing: border-box; }
  html, body {
    width: 1200px; height: 900px; overflow: hidden;
    background: var(--stage);
    font-family: "Roboto", Arial, sans-serif;
  }
  .card {
    position: absolute;
    left: 320px;
    width: 560px; height: 320px;
    border-radius: 18px;
    overflow: hidden;
    box-shadow: 0 10px 24px rgba(0,0,0,0.35);
  }
  /* Front side */
  .card--front { top: 95px; background: var(--brand-green); color: var(--card-white); }
  .front__brand {
    position: absolute; left: 0; right: 0; top: 108px;
    display: flex; align-items: center; justify-content: center; gap: 16px;
  }
  .brand__dot {
    width: 30px; height: 30px; border-radius: 50%;
    background: var(--brand-yellow);
  }
  .front__name {
    font-weight: 700; font-size: 64px; letter-spacing: 0.5px;
    color: var(--card-white);
  }
  .front__web {
    position: absolute; left: 42px; bottom: 34px;
    font-size: 19px; font-weight: 400; color: var(--card-white);
  }
  /* Back side */
  .card--back { top: 485px; background: var(--card-white); color: var(--ink); }
  .back__brand {
    position: absolute; left: 40px; top: 30px;
    display: flex; align-items: center; gap: 10px;
  }
  .back__brand .brand__dot { width: 18px; height: 18px; }
  .back__brand-name { font-weight: 700; font-size: 32px; color: var(--brand-green); }
  .person { position: absolute; left: 40px; top: 100px; }
  .person__name { font-weight: 700; font-size: 26px; color: var(--brand-green); }
  .person__title { font-size: 12px; font-weight: 500; color: var(--ink); margin-top: 2px; }
  .divider {
    position: absolute; left: 40px; right: 40px; top: 158px;
    height: 2px; background: var(--brand-green);
  }
  .contacts { position: absolute; left: 40px; top: 176px; list-style: none; }
  .contacts__item {
    display: flex; align-items: center; gap: 10px;
    font-size: 16px; line-height: 27px; color: var(--ink);
  }
  .contacts__icon { width: 14px; height: 14px; flex: none; }
  .location {
    position: absolute; right: 40px; bottom: 34px;
    display: flex; align-items: center; gap: 12px;
    font-size: 18px; color: var(--ink);
  }
  .location__badge {
    width: 46px; height: 46px; border-radius: 50%;
    background: #2a2a2a; border: 3px solid #9a9a9a;
  }
</style>
</head>
<body>

  <section class="card card--front" aria-label="Card front">
    <div class="front__brand">
      <span class="brand__dot"></span>
      <span class="front__name">Velmorin</span>
    </div>
    <p class="front__web">www.velmorin.com.au</p>
  </section>

  <section class="card card--back" aria-label="Card back">
    <div class="back__brand">
      <span class="brand__dot"></span>
      <span class="back__brand-name">Velmorin</span>
    </div>

    <div class="person">
      <h1 class="person__name">Tomas Brevik</h1>
      <p class="person__title">Managing Director</p>
    </div>

    <div class="divider"></div>

    <ul class="contacts">
      <li class="contacts__item">
        <svg class="contacts__icon" viewBox="0 0 24 24" aria-hidden="true">
          <path fill="#0b6544" d="M6.6 10.8a15 15 0 0 0 6.6 6.6l2.2-2.2c.3-.3.7-.4 1-.2 1.1.4 2.3.6 3.6.6.6 0 1 .4 1 1V20c0 .6-.4 1-1 1A17 17 0 0 1 3 4c0-.6.4-1 1-1h3.5c.6 0 1 .4 1 1 0 1.3.2 2.5.6 3.6.1.3 0 .7-.2 1z"/>
        </svg>
        +61 491058263
      </li>
      <li class="contacts__item">
        <svg class="contacts__icon" viewBox="0 0 24 24" aria-hidden="true">
          <rect x="2" y="5" width="20" height="14" rx="2" fill="#0b6544"/>
          <path d="M3 6l9 7 9-7" fill="none" stroke="#fff" stroke-width="1.6"/>
        </svg>
        tomas@velmorin.com.au
      </li>
      <li class="contacts__item">
        <svg class="contacts__icon" viewBox="0 0 24 24" aria-hidden="true">
          <circle cx="12" cy="12" r="10" fill="#0b6544"/>
          <path d="M2 12h20M12 2c3 3 3 17 0 20M12 2c-3 3-3 17 0 20" fill="none" stroke="#fff" stroke-width="1.4"/>
        </svg>
        www.velmorin.com.au
      </li>
    </ul>

    <div class="location">
      <span class="location__badge" role="img" aria-label="City badge"></span>
      <span>Melbourne, Australia</span>
    </div>
  </section>

</body>
</html>
```